Velvet Bloom Marisol's Cleaning Service Business Cards Project

A business card with all contact details with logo design on there (already have a logo) eye catching Logo and contact info on one side, full logo on the back, must target upper class residential and corporate companies, fitness companies, still keep it on the feminine side of things , must look elegant

Target Market(s)

Upper class homes and corporate companies

Industry/Entity Type

Cleaning Service

Contact Information for Business Card

Name: Marisol Denhart
Position: Director
ABN: 47193062857
Email: marisolsvelvetcleaning@brightmail.example
Number: 0418926547

Font styles to use
Decorative

Colors

Designer to choose colors to be used in the design.

Requirements
Must have
• Available Sydney Wide, contact info and logo on one side, full logo on the back
Nice to have
• Professional appearance
Should not have
• Cheap advert looking stuff

```html
<!DOCTYPE html>
<html lang="en">
<head>
<meta charset="utf-8">
<title>Velvet Bloom – Business Cards</title>
<link rel="stylesheet" href="https://fonts.googleapis.com/css2?family=Libre+Baskerville:wght@400;700&family=Tinos:wght@400&display=swap">
<style>
  :root {
    --backdrop: #3b3c3f;
    --card-light: #ffffff;
    --card-dark: #2e3240;
    --ink-navy: #262b3a;
    --accent-teal: #3fe0d2;
    --text-light: #f3f4f6;
  }
  * { margin: 0; padding: 0; box-sizing: border-box; }
  html, body {
    width: 1200px;
    height: 1000px;
    overflow: hidden;
    background: var(--backdrop);
  }
  .canvas {
    position: relative;
    width: 1200px;
    height: 1000px;
  }
  .card {
    position: absolute;
    width: 700px;
    height: 400px;
    border-radius: 26px;
    box-shadow: 0 18px 40px rgba(0,0,0,0.35);
  }
  .card--front {
    left: 420px;
    top: 70px;
    background: var(--card-light);
  }
  .card--back {
    left: 80px;
    top: 530px;
    background: var(--card-dark);
  }
  .brand {
    position: absolute;
    text-align: center;
    font-family: "Libre Baskerville", serif;
    font-weight: 400;
  }
  .card--front .brand {
    left: 0;
    right: 0;
    top: 150px;
    color: var(--ink-navy);
  }
  .brand__name {
    display: block;
    font-size: 46px;
    letter-spacing: 2px;
    text-transform: uppercase;
  }
  .brand__tagline {
    display: block;
    font-size: 15px;
    letter-spacing: 6px;
    text-transform: uppercase;
    margin-top: 12px;
  }
  .card--back .brand {
    left: 30px;
    width: 300px;
    top: 160px;
    color: var(--accent-teal);
  }
  .card--back .brand__name { font-size: 27px; letter-spacing: 1px; }
  .card--back .brand__tagline { font-size: 9px; letter-spacing: 3px; margin-top: 8px; }
  .divider {
    position: absolute;
    left: 360px;
    top: 60px;
    width: 2px;
    height: 280px;
    background: var(--accent-teal);
  }
  .contact {
    position: absolute;
    left: 392px;
    top: 96px;
    font-family: "Tinos", serif;
    color: var(--text-light);
  }
  .contact__name {
    font-family: "Libre Baskerville", serif;
    font-weight: 700;
    font-size: 24px;
    color: var(--accent-teal);
  }
  .contact__role {
    font-size: 18px;
    margin-top: 2px;
  }
  .contact__list {
    list-style: none;
    margin-top: 38px;
    font-size: 17px;
    line-height: 1.5;
  }
  .contact__item {
    display: flex;
    align-items: center;
    gap: 8px;
    white-space: nowrap;
  }
  .contact__icon { width: 14px; height: 14px; flex: none; }
  .contact__email { font-size: 14px; }
</style>
</head>
<body>
<main class="canvas">

  <section class="card card--front" aria-label="Card front">
    <div class="brand">
      <span class="brand__name">Velvet Bloom</span>
      <span class="brand__tagline">Marisol's Cleaning Service</span>
    </div>
  </section>

  <section class="card card--back" aria-label="Card back">
    <div class="brand">
      <span class="brand__name">Velvet Bloom</span>
      <span class="brand__tagline">Marisol's Cleaning Service</span>
    </div>

    <div class="divider"></div>

    <div class="contact">
      <p class="contact__name">Marisol Denhart</p>
      <p class="contact__role">Director</p>
      <ul class="contact__list">
        <li class="contact__item">ABN: 47193062857</li>
        <li class="contact__item">
          <svg class="contact__icon" viewBox="0 0 14 14" aria-hidden="true">
            <rect x="1" y="3" width="12" height="9" rx="1.5" fill="var(--accent-teal)"/>
            <path d="M1.5 3.8 L7 8 L12.5 3.8" fill="none" stroke="var(--card-dark)" stroke-width="1.2"/>
          </svg>
          <span class="contact__email">marisolsvelvetcleaning@brightmail.example</span>
        </li>
        <li class="contact__item">
          <svg class="contact__icon" viewBox="0 0 14 14" aria-hidden="true">
            <path d="M3 1.5 L5.2 1.5 L6 4.5 L4.6 5.6 C5.4 7.4 6.6 8.6 8.4 9.4 L9.5 8 L12.5 8.8 L12.5 11 C12.5 12 11.7 12.6 10.8 12.5 C5.8 12 2 8.2 1.5 3.2 C1.4 2.3 2 1.5 3 1.5 Z" fill="var(--accent-teal)"/>
          </svg>
          0418926547
        </li>
      </ul>
    </div>
  </section>

</main>
</body>
</html>
```